Lotvantage.com Webpage Design

Design Brief for lotvantage.com (Copy of Brief also in attached Word file)

Name of Website- lotvantage.com (existing logo and look & feel of website to be changed)

Logo - Finalised. The logo files are attached with the brief as “logo.jpeg”. The “Blue- Grey” version of the logo is for use on lighter backgrounds and the “Orange-White” version of the logo is for use on darker backgrounds. (A full Black version of the logo is also attached). Both versions may be used in different parts of the website. All attached files are in .png format.
Status - The website in functional and is undergoing user trials. However, we want to improve the look & feel of the website so at it seems
a. cotemporary,
b. Easy to Navigate
c. professional and
d. Vibrant.

Please visit ‘lotvantage.com’ to check out the website and its functionalities – please use it only as a reference for the features & functions to be provided, however the designer should use a ‘Free Hand’ in designing the composition of various parts of the webpage without getting too influenced by the existing design

Objective of the Website ‘lotvantage.com –
a. It is a portal focussed on listing of ‘Retail’ specific real-estate properties by developers, owners and realty brokers. The properties shall listed under the following four categories-
i. Retail Malls
ii. Shopping Complexes
iii. High-street shops
iv. Retail Warehouses
*refer lotvantage.com for better clarity

b. The abovementioned properties shall be listed either for ‘Sale’ or ‘rent\lease’ or both

c. Users shall visit the site in case they wish to acquire a retail \ shop space either on ‘sale’ or ‘rent’. These Users would be able to specify the ‘Search Criteria’ through the tool-bars provided on the website – the ‘Search Criteria’ shall comprise of ‘Type of space category’, ‘City’, ‘Locality’, transaction type ie ‘Rent \ Sale’ and ‘Area Range’

d. The main revenue model for the website shall be listing fee ( or advertising charges ) payable by those listing their properties on the website.

Three Main Pages of Website (lotvantage.com) that need to be designed -
a. Main Home Page (visit the web link - http://lotvantage.com/ ) - The main home page has the “Search Toolbar” for specifying of Search Criteria by the User. It shall also have the following features & functions-
i. Main Advertising Banner
ii. Featured Projects
iii. New Launches
iv. Toolbar with buttons – ‘Advertise with Us’, ‘Listings Alert’, ‘Lot Mavens’, ‘Advertiser Login’

b. Property Listings Page (visit the web link - http://lotvantage.com/gurgaon-in-india ) - The List of property options that match the Criteria specified by the ‘User’ get displayed on this page.

c. Property Detail Page - When the ‘User’ clicks on the “More….” Button on the ‘Property Listings Page’ (given in point b. above) the web page with the details of the property opens. (For Example – visit the web link - http://lotvantage.com/brevo-Shopping-Complex-brevo-quadrel-gurgaon-636 )

Note:- Please refer to attached ‘Shopping’ related images the designer may use them on the website to provide a look & feel of retail if required – either separately or rotate in a single window

Target Market(s)

Retailers & Investors looking for retail space, Real Estate Brokers, Developers

Industry/Entity Type

Advertising

Number of Pages Required

3 page

Requirements
Must have
• Refer to existing site lotvantage.com -- all the existing functionalities are a must have.
Nice to have
• The Designer may use the retail related images on the website if required for making it more vibrant. Refer attached images Shopping(1-6).jpg

```html
<!DOCTYPE html>
<html lang="en">
<head>
<meta charset="utf-8">
<title>Lotvantage.com – Retail Space Portal</title>
<link rel="stylesheet" href="https://fonts.googleapis.com/css2?family=Arimo:wght@400;700&family=Lato:wght@300;400;700&display=swap">
<style>
:root{
  --blue:#1a8fe0;
  --blue-deep:#0d63b0;
  --orange:#f2a531;
  --orange-dark:#e89520;
  --dark:#4f4f4f;
  --panel:#5b5b5b;
  --text:#333;
  --muted:#555;
  --light:#f2f2f2;
  --footer:#0d63b0;
  --bottom:#4a4a4a;
  --white:#fff;
}
*{box-sizing:border-box;margin:0;padding:0}
html,body{width:1200px;height:2695px;overflow:hidden}
body{font-family:"Arimo",Arial,sans-serif;color:var(--text);background:var(--white);font-size:13px;position:relative}
.wrap{width:980px;margin:0 auto;position:relative}

/* city bar */
.city-bar{height:22px;background:var(--blue);display:flex;justify-content:center;align-items:center;gap:24px;color:var(--white);font-size:12px}

/* header */
.site-header{height:100px;position:relative}
.brand{position:absolute;left:110px;top:22px;display:flex;align-items:center;gap:8px}
.brand-dot{width:34px;height:34px;border-radius:50%;background:var(--orange)}
.brand-name{font-family:"Lato",sans-serif;font-weight:700;font-size:30px;color:var(--blue-deep)}
.brand-tag{position:absolute;left:154px;top:64px;font-size:8px;letter-spacing:.5px;color:var(--blue-deep);font-weight:700}
.nav{position:absolute;top:34px;font-size:12px;line-height:1.35;text-align:center}
.nav .hl{color:var(--blue-deep)}
.nav-advertise{left:446px;display:flex;gap:10px;text-align:left}
.nav-mavens{left:652px}
.nav-alert{left:818px;color:var(--blue-deep)}
.account{position:absolute;right:122px;top:14px;text-align:center;font-size:12px;color:var(--blue-deep);line-height:1.3}
.btn-login{display:block;margin:6px auto;background:var(--blue-deep);color:var(--white);font-weight:700;padding:5px 10px;border-radius:3px;width:110px}

/* hero */
.hero{height:539px;background:linear-gradient(90deg,#f4f4f4,#fafafa 60%,#eee);position:relative;border-bottom:1px solid #ddd}
.hero-photo{position:absolute;left:110px;top:36px;width:664px;height:455px;background:linear-gradient(160deg,#6b5a3e,#2d2620 55%,#4b3c2c)}
.feature-box{position:absolute;left:360px;top:297px;width:414px;background:rgba(255,255,255,.88)}
.feature-box h2{font-family:"Lato",sans-serif;font-size:20px;color:var(--blue);font-weight:700;padding:10px 26px 6px}
.feature-box p{font-size:14px;line-height:1.3;padding:0 26px 10px;color:#222}
.feature-box p a{color:var(--orange);text-decoration:none}
.feature-tabs{display:flex;font-size:13px;color:var(--white)}
.feature-tabs span{padding:10px 0;text-align:center}
.tab-city{background:#3a3a3a;width:118px}
.tab-type{background:var(--blue);width:136px}
.tab-alt{background:var(--orange);width:160px}

.search{position:absolute;left:790px;top:36px;width:300px;height:455px;background:var(--orange-dark);padding:14px 22px;color:var(--white);font-size:11px}
.search h3{text-align:center;font-size:14px;font-weight:400}
.search h3 .sub{display:block;color:var(--blue-deep);margin-top:2px}
.checks{display:grid;grid-template-columns:1fr 1fr;gap:10px 6px;margin:14px 0 16px}
.checks span{display:flex;align-items:center;gap:6px}
.checks i{width:11px;height:11px;background:var(--white);display:inline-block}
.field-label{display:block;margin:12px 0 8px}
.select{height:28px;background:var(--white);border-radius:14px;color:#333;font-size:11px;display:flex;align-items:center;justify-content:space-between;padding:0 0 0 10px}
.select i{width:28px;height:28px;border-radius:50%;background:#2c2c2c;display:flex;align-items:center;justify-content:center}
.input-pill{height:28px;background:var(--white);border-radius:14px;color:#333;display:flex;align-items:center;padding-left:10px;font-size:11px}
.btn-search{display:block;width:140px;margin:24px auto 0;background:#3a3a3a;text-align:center;padding:9px 0;font-weight:700;font-size:15px}

/* services */
.services{height:390px;text-align:center}
.section-title{font-family:"Lato",sans-serif;font-weight:400;font-size:38px;color:var(--blue);padding-top:40px}
.service-grid{display:grid;grid-template-columns:repeat(4,215px);justify-content:space-between;margin-top:42px}
.service-icon{width:80px;height:80px;border-radius:50%;background:var(--blue);margin:0 auto;display:flex;align-items:center;justify-content:center}
.service h4{font-size:15px;font-weight:400;margin:24px 0 12px;letter-spacing:.3px}
.service p{font-size:13px;line-height:1.5;color:#333}

/* featured */
.featured{height:392px;position:relative}
.featured.shade{background:linear-gradient(90deg,#f0f0f0,#fbfbfb 50%,#eee);border-top:1px solid #ddd}
.featured h2{font-family:"Lato",sans-serif;font-weight:400;font-size:32px;color:var(--blue-deep);padding-top:42px}
.featured h2 small{font-size:14px;color:#333}
.cards{display:grid;grid-template-columns:repeat(4,215px);gap:40px;margin-top:20px}
.card{background:var(--white);border:1px solid #ddd;height:221px;padding:6px 6px 0}
.card-photo{height:135px;position:relative;background:linear-gradient(180deg,#7a9ac0,#9aa4ae 60%,#6d6f70)}
.price{position:absolute;left:0;bottom:0;background:var(--blue);color:var(--white);font-size:12px;padding:3px 4px}
.for-sale{position:absolute;right:0;bottom:0;background:var(--orange);color:var(--white);font-size:12px;padding:3px 8px;width:64px}
.card-row{display:flex;justify-content:space-between;align-items:baseline;font-size:12px;padding:0 2px}
.card-row:nth-of-type(2){margin-top:6px;border-bottom:1px solid #ddd;padding-bottom:6px}
.card-row:nth-of-type(3){margin-top:10px}
.card-row b{color:var(--blue);font-size:15px}
.arrow{position:absolute;top:255px;width:28px;height:28px;border-radius:50%;border:1px solid #333;background:var(--white);display:flex;align-items:center;justify-content:center}
.arrow.prev{left:60px}.arrow.next{left:1114px}

/* widgets */
.widgets{height:469px;background:var(--light);padding-top:38px}
.widget-row{display:flex;justify-content:space-between}
.panel{background:var(--panel);color:var(--white);height:383px;border:1px solid #444;padding:12px 14px;font-size:12px;position:relative}
.panel h3,.editors h3{font-family:"Lato",sans-serif;font-weight:400;font-size:25px;padding-bottom:8px;border-bottom:1px solid #999;width:82%}
.alert{width:325px}
.mavens{width:271px}
.alert-intro{display:flex;align-items:center;gap:14px;margin:20px 0 22px;line-height:1.4}
.w-input{height:28px;background:var(--white);color:#333;border:1px solid #bbb;display:flex;align-items:center;justify-content:space-between;padding-left:8px;font-size:12px;margin-bottom:8px}
.hint{margin:10px 0 22px}
.btn-orange{position:absolute;background:var(--orange);color:var(--white);font-size:13px;font-weight:700;text-align:center;padding:7px 0}
.editors{width:307px;position:relative}
.editors h3{color:var(--blue);border-bottom-color:var(--blue);width:100%}
.editors-photo{height:125px;margin-top:20px;background:linear-gradient(135deg,#c23a3a,#e6b85c 50%,#8fb6d6)}
.editors p{font-size:12px;line-height:1.4;margin-top:10px}
.mavens p{line-height:1.5;margin:14px 0 16px}
.area{height:64px;align-items:flex-start;padding-top:6px}

/* footer */
.site-footer{height:354px;background:var(--footer);color:var(--white);position:relative}
.f-col{position:absolute;top:28px}
.f-col h4{font-family:"Lato",sans-serif;font-size:19px;font-weight:700;padding-bottom:12px;border-bottom:1px solid rgba(255,255,255,.5);width:180px;margin-bottom:26px}
.f-links li{list-style:none;font-size:13px;margin-bottom:12px}
.f-links li::before{content:"› "}
.f-col p{font-size:12px;line-height:1.6}
.f-btn{display:inline-block;background:var(--orange);padding:7px 12px;font-size:11px;margin-top:16px}
.news-row{display:flex;margin-top:28px;font-size:12px}
.news-row span:first-child{background:#555;width:140px;padding:9px 6px}
.news-row span:last-child{background:var(--orange);padding:9px 8px}
.contact li{list-style:none;font-size:12px;line-height:1.5;margin-bottom:14px;display:flex;gap:8px}
.footer-brand{position:absolute;left:853px;top:252px;display:flex;align-items:center;gap:8px}
.footer-brand .brand-name{color:var(--white)}

.bottom-bar{height:54px;background:var(--bottom);color:var(--white);display:flex;align-items:center;justify-content:space-between;padding:0 110px;font-size:12px}
.social{display:flex;gap:9px}
.social i{width:26px;height:26px;background:#bdbdbd;display:block}
</style>
</head>
<body>

<nav class="city-bar">
  <span>Bangalore</span><span>Chennai</span><span>Greater Nodia</span><span>Gurgaon</span><span>Hyderabad</span><span>Jaipur</span><span>Khanna</span><span>Kolkatta</span><span>Mumbai</span><span>Nodia</span><span>Pune</span><span>Surat</span>
</nav>

<header class="site-header">
  <div class="brand"><span class="brand-dot"></span><span class="brand-name">lotvantage</span></div>
  <div class="brand-tag">INDIA'S LEADING PORTAL FOR RETAIL SPACE</div>
  <div class="nav nav-advertise">
    <svg width="26" height="24" viewBox="0 0 26 24"><path d="M2 12 13 2l11 10M6 10v12h14V10" fill="none" stroke="#0d63b0" stroke-width="2"/></svg>
    <div><span class="hl">Avertise with us</span><br>Standard listing - FREE</div>
  </div>
  <div class="nav nav-mavens"><span class="hl">Lot Mavens</span><br>Shop Search Services</div>
  <div class="nav nav-alert">Listing Alert</div>
  <div class="account">List Your Property Here<span class="btn-login">Advertiser Login</span>New Advertiser - Register</div>
</header>

<section class="hero">
  <div class="hero-photo" role="img" aria-label="Shoppers walking through a lit-up retail arcade at night"></div>
  <div class="feature-box">
    <h2>FEATURED RETAIL PROJECTS</h2>
    <p>Model sentence structures, to generate Lorem Ipsum which looks reasonable. The generated Lorem Ipsum is therefore always free. <a href="#">read more</a></p>
    <div class="feature-tabs"><span class="tab-city">Gurgaon</span><span class="tab-type">Shopping Complex</span><span class="tab-alt">Retail Wearhouse</span></div>
  </div>
  <form class="search">
    <h3>Select Retail Format:<span class="sub">Meaning of Retail Format</span></h3>
    <div class="checks">
      <span><i></i>Retail Malls</span><span><i></i>Shopping Complex</span>
      <span><i></i>High Street shops</span><span><i></i>Retail Wear houses</span>
    </div>
    <span class="field-label">Sale Or Rent Or BOTH:</span>
    <div class="select">Both<i><svg width="10" height="6"><path d="M0 0h10L5 6z" fill="#fff"/></svg></i></div>
    <span class="field-label">Select City:</span>
    <div class="select">--Select--<i><svg width="10" height="6"><path d="M0 0h10L5 6z" fill="#fff"/></svg></i></div>
    <span class="field-label">Select Locality/Micro-Market:</span>
    <div class="select">--Select--<i><svg width="10" height="6"><path d="M0 0h10L5 6z" fill="#fff"/></svg></i></div>
    <span class="field-label">Enter Key words:</span>
    <div class="input-pill">Name of project, Developer etc</div>
    <span class="btn-search">SEARCH</span>
  </form>
</section>

<section class="services">
  <div class="wrap">
    <h2 class="section-title">OUR SERVICES</h2>
    <div class="service-grid">
      <div class="service">
        <div class="service-icon"><svg width="36" height="32" viewBox="0 0 36 32"><path d="M18 2 2 16h5v14h8v-9h6v9h8V16h5z" fill="#fff"/></svg></div>
        <h4>SHOPPING COMPLEXES</h4>
        <p>Lorem ipsum dolor is consectetur adipiscing elit the sed do eiusmod tempor incididunt ut the labore et dolore magna aliqua.</p>
      </div>
      <div class="service">
        <div class="service-icon"><svg width="36" height="36" viewBox="0 0 36 36"><circle cx="16" cy="11" r="7" fill="#fff"/><path d="M4 32c0-8 5-12 12-12s12 4 12 12z" fill="#fff"/><circle cx="26" cy="14" r="5" fill="none" stroke="#fff" stroke-width="2"/></svg></div>
        <h4>RETAIL MALLS</h4>
        <p>Lorem ipsum dolor is consectetur adipiscing elit the sed do eiusmod tempor incididunt ut the labore et dolore magna aliqua.</p>
      </div>
      <div class="service">
        <div class="service-icon"><svg width="32" height="34" viewBox="0 0 32 34"><rect x="4" y="8" width="10" height="24" fill="#fff"/><rect x="16" y="2" width="12" height="30" fill="#fff"/><path d="M18 6h8M18 11h8M18 16h8M18 21h8M6 12h6M6 17h6M6 22h6" stroke="#1a8fe0" stroke-width="2"/></svg></div>
        <h4>RETAIL WAREHOUSES</h4>
        <p>Lorem ipsum dolor is consectetur adipiscing elit the sed do eiusmod tempor incididunt ut the labore et dolore magna aliqua.</p>
      </div>
      <div class="service">
        <div class="service-icon"><svg width="40" height="34" viewBox="0 0 40 34"><circle cx="20" cy="7" r="5" fill="#fff"/><circle cx="9" cy="10" r="4" fill="#fff"/><circle cx="31" cy="10" r="4" fill="#fff"/><path d="M14 32V18a6 6 0 0 1 12 0v14zM3 32V21a6 6 0 0 1 9-3v14zM37 32V21a6 6 0 0 0-9-3v14z" fill="#fff"/></svg></div>
        <h4>HIGH STREET SHOPS</h4>
        <p>Lorem ipsum dolor is consectetur adipiscing elit the sed do eiusmod tempor incididunt ut the labore et dolore magna aliqua.</p>
      </div>
    </div>
  </div>
</section>

<section class="featured shade">
  <div class="wrap">
    <h2>Featured Retail Project <small>Across India</small></h2>
    <div class="cards">
      <article class="card"><div class="card-photo" role="img" aria-label="Curved glass commercial tower"><span class="price">$2,100.00</span><span class="for-sale">For Sale</span></div><div class="card-row"><b>Halvern Trinity</b><span>NH Bypass</span></div><div class="card-row"><span>Gurgaon</span><span>Dwarka Expressway</span></div></article>
      <article class="card"><div class="card-photo" role="img" aria-label="Low-rise mall building at dusk"><span class="price">$2,100.00</span><span class="for-sale">For Sale</span></div><div class="card-row"><b>Mysore</b><span>Hunsur Main Road</span></div><div class="card-row"><span>Elmgate Mall</span><span>Retail Malls</span></div></article>
      <article class="card"><div class="card-photo" role="img" aria-label="Red brick shopping complex"><span class="price">$2,100.00</span><span class="for-sale">For Sale</span></div><div class="card-row"><b>Noida</b><span>NH Bypass</span></div><div class="card-row"><span>Crestline One</span><span>Shopping Complex</span></div></article>
      <article class="card"><div class="card-photo" role="img" aria-label="Illuminated mall facade at night"><span class="price">$2,100.00</span><span class="for-sale">For Sale</span></div><div class="card-row"><b>Bhopal</b><span>Klora Road</span></div><div class="card-row"><span>The Grand Market Place</span><span>Retail Mall</span></div></article>
    </div>
  </div>
  <span class="arrow prev"><svg width="8" height="12"><path d="M7 1 2 6l5 5" fill="none" stroke="#333" stroke-width="2"/></svg></span>
  <span class="arrow next"><svg width="8" height="12"><path d="m1 1 5 5-5 5" fill="none" stroke="#333" stroke-width="2"/></svg></span>
</section>

<section class="featured">
  <div class="wrap">
    <h2>Featured Retail Project <small>Across India</small></h2>
    <div class="cards">
      <article class="card"><div class="card-photo" role="img" aria-label="Curved glass commercial tower"><span class="price">$2,100.00</span><span class="for-sale">For Sale</span></div><div class="card-row"><b>Halvern Trinity</b><span>NH Bypass</span></div><div class="card-row"><span>Gurgaon</span><span>Dwarka Expressway</span></div></article>
      <article class="card"><div class="card-photo" role="img" aria-label="Low-rise mall building at dusk"><span class="price">$2,100.00</span><span class="for-sale">For Sale</span></div><div class="card-row"><b>Mysore</b><span>Hunsur Main Road</span></div><div class="card-row"><span>Elmgate Mall</span><span>Retail Malls</span></div></article>
      <article class="card"><div class="card-photo" role="img" aria-label="Red brick shopping complex"><span class="price">$2,100.00</span><span class="for-sale">For Sale</span></div><div class="card-row"><b>Noida</b><span>NH Bypass</span></div><div class="card-row"><span>Crestline One</span><span>Shopping Complex</span></div></article>
      <article class="card"><div class="card-photo" role="img" aria-label="Illuminated mall facade at night"><span class="price">$2,100.00</span><span class="for-sale">For Sale</span></div><div class="card-row"><b>Bhopal</b><span>Klora Road</span></div><div class="card-row"><span>The Grand Market Place</span><span>Retail Mall</span></div></article>
    </div>
  </div>
  <span class="arrow prev"><svg width="8" height="12"><path d="M7 1 2 6l5 5" fill="none" stroke="#333" stroke-width="2"/></svg></span>
  <span class="arrow next"><svg width="8" height="12"><path d="m1 1 5 5-5 5" fill="none" stroke="#333" stroke-width="2"/></svg></span>
</section>

<section class="widgets">
  <div class="wrap widget-row">
    <div class="panel alert">
      <h3>Listing Alert</h3>
      <div class="alert-intro">
        <svg width="48" height="32" viewBox="0 0 48 32"><rect x="1" y="1" width="46" height="30" fill="#eee"/><path d="m1 1 23 17L47 1" fill="none" stroke="#999" stroke-width="2"/></svg>
        <span>Suscribe for Fortnightly Email update on New Listing @Lotvantage</span>
      </div>
      <div class="w-input">Enter your Email adress</div>
      <div class="w-input" style="margin-top:14px">Select option<svg width="20" height="10"><path d="M5 2h10l-5 6z" fill="#555"/></svg></div>
      <div class="hint" style="margin-top:8px">(Select retail formate of Intrest)</div>
      <div class="w-input"> <svg width="20" height="10"><path d="M5 2h10l-5 6z" fill="#555"/></svg></div>
      <div style="margin-top:8px">(Select cities of Intrest)</div>
      <span class="btn-orange" style="left:220px;top:334px;width:88px">Subscribe</span>
    </div>
    <div class="editors">
      <h3>Editor’s Choice</h3>
      <div class="editors-photo" role="img" aria-label="Family holding shopping bags in a store"></div>
      <p>A "Select" Listing of Retail Properties Handpicked by our Editors based on their own positive evaluation on parameters &amp; attributes such as Design Concept, Location, Developer, Success Potential. So Read On to Check Out for yourself ...........</p>
      <span class="btn-orange" style="left:213px;top:355px;width:90px">More</span>
    </div>
    <div class="panel mavens">
      <h3>Lot Mavens</h3>
      <p>Post your Retail Space requirement with us and our experts shall get back with suitable options and even help you in your transaction. This is a Free Service!</p>
      <div class="w-input">Enter yor email adress:</div>
      <div class="w-input" style="margin-top:10px">Mobile</div>
      <div class="w-input area">Add Description of requirment</div>
      <span class="btn-orange" style="left:162px;top:334px;width:90px">Send</span>
    </div>
  </div>
</section>

<footer class="site-footer">
  <div class="f-col" style="left:110px">
    <h4 style="width:140px">About Us</h4>
    <ul class="f-links"><li>About Us</li><li>Privacy Policy</li><li>terms of Uses</li><li>Contact Us</li><li>Site Map</li><li>Retail Malls</li><li>Shopping Complex</li></ul>
  </div>
  <div class="f-col" style="left:298px;width:250px">
    <h4 style="width:150px">About Estate</h4>
    <p>Latin words, combined with a handful of model sentence structures, to generate Lorem Ipsum which looks reasonable. The generated Lorem Ipsum is therefore always</p>
    <span class="f-btn">Read More</span>
  </div>
  <div class="f-col" style="left:595px;width:220px">
    <h4 style="width:200px">News Letter Form</h4>
    <p>Latin words, combined with a handful of model sentence structures, to generate.</p>
    <div class="news-row"><span>Enter Email</span><span>Subscribe</span></div>
  </div>
  <div class="f-col" style="left:861px;width:230px">
    <h4>CONTACT INFO</h4>
    <ul class="contact">
      <li>42, C Block, Marlow Lane, Eastbridge, EBK, Northland</li>
      <li><svg width="12" height="12" viewBox="0 0 12 12"><path d="M2 1h3l1 3-2 1a7 7 0 0 0 3 3l1-2 3 1v3c-6 0-10-4-10-9z" fill="#fff"/></svg>Phone : 1800-555-019-47</li>
      <li><svg width="12" height="12"><rect x="1" y="2" width="10" height="8" fill="none" stroke="#fff"/><path d="m1 2 5 4 5-4" fill="none" stroke="#fff"/></svg>Email : hello@lotvantage.com</li>
      <li><svg width="12" height="12"><circle cx="6" cy="6" r="5" fill="none" stroke="#fff"/><path d="M1 6h10M6 1v10" stroke="#fff"/></svg>Website : lotvantage.com</li>
    </ul>
  </div>
  <div class="footer-brand"><span class="brand-dot"></span><span class="brand-name">lotvantage</span></div>
</footer>

<div class="bottom-bar">
  <span>Parcel+ a real estate template. Copyright 2015</span>
  <div class="social"><i></i><i></i><i></i><i></i><i></i></div>
</div>

</body>
</html>
```